Cobalt Homes Web Site Design

improve on the graphic design on our current website
www.cobalthmoes.com.au
wordpress required

Graphic Design

Coding

Coded - Design and coding required

Number of Pages Required

5+ page

```html
<!DOCTYPE html>
<html lang="en">
<head>
<meta charset="utf-8">
<title>Cobalt Homes – Canberra's Boutique Builders</title>
<link href="https://fonts.googleapis.com/css2?family=Roboto:wght@300;400;500;700&family=Roboto+Condensed:wght@400;700&family=Open+Sans:wght@400;600&display=swap" rel="stylesheet">
<style>
:root{
  --red:#c41f2f;
  --ink:#2b2b2b;
  --text:#555;
  --muted:#888;
  --light:#ebebeb;
  --white:#fff;
  --footer:#a3a3a3;
  --dark-overlay:#2e3134;
}
*{box-sizing:border-box;margin:0;padding:0}
html,body{width:1200px;height:3956px;overflow:hidden}
body{font-family:"Open Sans",sans-serif;color:var(--text);background:var(--white);position:relative}
.red{color:var(--red)}
section,header,footer{position:relative;width:1200px;overflow:hidden}

/* Hero */
.hero{height:800px}
.hero-photo{position:absolute;inset:0;background:linear-gradient(180deg,#d9d9d9 0%,#cfcfcf 45%,#7a6a5c 70%,#3d2f26 100%)}
.topbar{position:absolute;top:0;left:0;right:0;height:118px;display:flex;align-items:center;justify-content:space-between;padding:0 80px 0 79px}
.brand{display:flex;align-items:center;gap:14px}
.brand-dot{width:74px;height:74px;border-radius:50%;background:var(--red)}
.brand-name{font-family:"Roboto",sans-serif;font-weight:500;font-size:34px;color:var(--ink);line-height:1}
.brand-sub{display:block;font-size:12px;font-weight:400;color:var(--ink);margin-top:4px;letter-spacing:.3px}
.nav{display:flex;gap:40px;font-family:"Roboto Condensed",sans-serif;font-size:18px;color:var(--ink);text-transform:uppercase}
.nav .active{color:var(--red)}
.hero-title{position:absolute;left:79px;top:258px;font-family:"Roboto Condensed",sans-serif;font-weight:700;font-size:64px;line-height:76px;color:#111;text-transform:uppercase}
.btn{display:inline-flex;align-items:center;justify-content:center;gap:8px;background:var(--red);color:var(--white);font-family:"Roboto Condensed",sans-serif;font-weight:700;font-size:22px;text-transform:uppercase}
.hero .btn{position:absolute;left:79px;top:436px;width:220px;height:60px}

/* Welcome */
.welcome{height:645px;text-align:center}
.section-title{font-family:"Roboto",sans-serif;font-weight:400;font-size:52px;color:#555}
.welcome .section-title{margin-top:62px}
.lead{font-size:15px;line-height:26px;color:var(--muted);width:980px;margin:0 auto}
.welcome .lead.first{margin-top:20px}
.welcome .lead.second{margin-top:20px}
.features{display:flex;justify-content:space-between;width:1040px;margin:46px auto 0}
.feature{width:320px}
.feature-icon{width:124px;height:124px;border-radius:50%;border:6px solid #c9c9c9;border-left-color:var(--red);border-top-color:var(--red);margin:0 auto;display:flex;align-items:center;justify-content:center;background:var(--white)}
.feature h3{font-family:"Roboto Condensed",sans-serif;font-weight:400;font-size:24px;color:var(--ink);text-transform:uppercase;margin-top:24px}
.feature p{font-size:15px;line-height:24px;color:var(--text);margin-top:12px}

/* Contact band */
.touch{height:470px;text-align:center;color:var(--white)}
.touch-photo{position:absolute;inset:0;background:linear-gradient(100deg,#3a3d40 0%,#2b2e31 50%,#4a4d50 100%)}
.touch-inner{position:relative}
.touch h2{font-family:"Roboto",sans-serif;font-weight:400;font-size:46px;margin-top:58px}
.touch p{font-size:16px;line-height:24px;width:1000px;margin:0 auto}
.touch p.gap{margin-top:26px}
.touch .intro{margin-top:10px}
.call{display:flex;align-items:center;justify-content:center;gap:26px;margin-top:34px;font-family:"Roboto",sans-serif;font-size:30px}
.call-icon{width:62px;height:62px;border:2px solid var(--white);border-radius:50%;display:flex;align-items:center;justify-content:center}
.touch .btn{width:182px;height:54px;margin-top:26px}

/* Services */
.services{height:379px;text-align:center}
.services .section-title{margin-top:46px}
.services .lead{margin-top:14px;font-size:15px;width:1000px}
.service-list{display:flex;justify-content:space-between;width:1060px;margin:30px auto 0}
.service{width:150px;font-family:"Roboto Condensed",sans-serif;font-size:20px;line-height:30px;color:var(--ink);text-transform:uppercase}
.service svg{display:block;margin:0 auto 10px}

/* Portfolio */
.portfolio{height:760px;background:var(--light);text-align:center}
.portfolio .section-title{margin-top:50px}
.tabs{display:flex;justify-content:center;gap:14px;margin-top:26px}
.tab{height:53px;background:var(--white);font-family:"Roboto Condensed",sans-serif;font-size:21px;color:var(--ink);text-transform:uppercase;display:flex;align-items:center;justify-content:center}
.tab.active{background:var(--red);color:var(--white)}
.grid{display:grid;grid-template-columns:repeat(4,240px);column-gap:29px;row-gap:34px;width:1047px;margin:18px auto 0}
.card{background:var(--white)}
.card .shot{height:185px}
.card .cap{height:42px;line-height:42px;color:var(--red);font-size:18px}
.s1{background:linear-gradient(160deg,#39434c,#a88a66)}
.s2{background:linear-gradient(170deg,#2d4f8a,#7e9a45)}
.s3{background:linear-gradient(170deg,#eeeeee,#6e6a66)}
.s4{background:linear-gradient(160deg,#d8dde0,#6e7479)}
.s5{background:linear-gradient(170deg,#f2f4f6,#9fb4c2)}
.s6{background:linear-gradient(170deg,#5a4a38,#2c2622)}
.s7{background:linear-gradient(170deg,#e8ecef,#7d8a8f)}
.s8{background:linear-gradient(170deg,#dfe4e9,#c9ccd0)}

/* Testimonial + quote */
.split{height:506px;display:flex;padding:0 79px}
.testimonial{width:480px}
.quote-form{margin-left:72px;width:490px}
.split h2{font-family:"Roboto",sans-serif;font-weight:400;font-size:50px;color:#555;margin-top:48px}
.quote-mark{font-family:"Roboto",sans-serif;font-weight:700;font-size:56px;color:var(--ink);line-height:40px;margin-top:22px;height:36px}
.testimonial p{font-size:15px;line-height:26px;color:var(--text);margin-top:14px}
.client{font-size:14px;font-weight:600;color:var(--red);text-transform:uppercase;margin-top:22px}
.arrows{display:flex;gap:14px;margin-top:20px}
.arrow{width:46px;height:46px;background:#3a3a3a;display:flex;align-items:center;justify-content:center}
.form{margin-top:22px;display:grid;grid-template-columns:1fr 1fr;gap:22px 22px}
.field{height:44px;border:1px solid #d4d4d4;background:#f8f8f8;font-size:14px;color:#888;padding:12px 10px}
.field.wide{grid-column:1/3}
.field.msg{height:104px}
.form .btn{width:136px;height:46px;font-weight:400;font-size:20px}

/* Banner */
.banner{height:124px;background:var(--red);display:flex;align-items:center;justify-content:space-between;padding:0 79px}
.banner p{font-family:"Roboto",sans-serif;font-size:34px;color:var(--white)}
.banner p b{font-weight:700}
.banner .cta{width:200px;height:54px;background:var(--white);color:var(--ink);font-family:"Roboto",sans-serif;font-size:20px;display:flex;align-items:center;justify-content:center;text-transform:uppercase}

/* Footer */
.footer{height:272px;background:var(--footer);color:var(--white);padding:0 79px}
.footer-top{display:flex;align-items:center;justify-content:space-between;height:100px;border-bottom:1px solid #c2c2c2}
.footer-nav{display:flex;gap:30px;font-size:15px;text-transform:uppercase}
.footer-nav .active{color:var(--red)}
.social{display:flex;gap:20px}
.social span{width:50px;height:50px;border-radius:50%;border:2px solid #ddd;display:flex;align-items:center;justify-content:center}
.social span i{width:26px;height:26px;border-radius:50%;background:var(--red);display:block}
.footer h4{font-family:"Roboto",sans-serif;font-weight:400;font-size:24px;color:var(--red);margin-top:28px}
.footer-info{display:flex;font-size:16px;line-height:24px;margin-top:4px}
.info{display:flex;gap:14px}
.info.addr{width:270px}
.info.tel{width:270px;font-weight:600;font-size:20px}
.info.mail{width:290px}
.info u{text-decoration:underline}
.copy{width:240px;display:flex;gap:6px}
.copy .red{color:var(--red)}
</style>
</head>
<body>

<header class="hero">
  <div class="hero-photo" role="img" aria-label="Photo of a bright modern bathroom with a freestanding tub on dark timber floor and a pebble rug"></div>
  <div class="topbar">
    <div class="brand">
      <span class="brand-dot"></span>
      <span class="brand-name">Cobalt Homes<span class="brand-sub">Homes &amp; Designs Pty Ltd</span></span>
    </div>
    <nav class="nav">
      <span class="active">Home</span><span>Company</span><span>Excellence</span><span>Experience</span><span>Expertise</span><span>Contact</span>
    </nav>
  </div>
  <h1 class="hero-title">Canberra's<br>Boutique Builders</h1>
  <a class="btn">Contact Us
    <svg width="14" height="18" viewBox="0 0 14 18"><path d="M3 2l8 7-8 7" fill="none" stroke="#fff" stroke-width="3"/></svg>
  </a>
</header>

<section class="welcome">
  <h2 class="section-title">Welcome to <span class="red">Cobalt Home Builders</span> Canberra</h2>
  <p class="lead first">Cobalt Homes is a boutique building company based in Canberra ACT.</p>
  <p class="lead second">Having been in the construction industry for many years have turned us into experts in the field. For any of your building and construction needs, please don't hesitate to contact us.</p>
  <div class="features">
    <div class="feature">
      <div class="feature-icon">
        <svg width="52" height="52" viewBox="0 0 52 52" fill="#c41f2f"><rect x="6" y="14" width="16" height="34"/><rect x="26" y="4" width="20" height="44"/><g fill="#fff"><rect x="10" y="20" width="3" height="4"/><rect x="15" y="20" width="3" height="4"/><rect x="10" y="30" width="3" height="4"/><rect x="15" y="30" width="3" height="4"/><rect x="31" y="12" width="4" height="4"/><rect x="38" y="12" width="4" height="4"/><rect x="31" y="22" width="4" height="4"/><rect x="38" y="22" width="4" height="4"/><rect x="31" y="32" width="4" height="4"/><rect x="38" y="32" width="4" height="4"/></g></svg>
      </div>
      <h3>Canberra Building Services</h3>
      <p>Cobalt Homes is a Canberra based building company focusing on first class residential homes and 100% client satisfaction.</p>
    </div>
    <div class="feature">
      <div class="feature-icon">
        <svg width="52" height="52" viewBox="0 0 52 52" fill="#c41f2f"><rect x="8" y="6" width="36" height="10" rx="3"/><rect x="14" y="18" width="24" height="12" rx="6"/><path d="M6 48c0-10 8-16 20-16s20 6 20 16z"/></svg>
      </div>
      <h3>Top Class Architects</h3>
      <p>Working with the best architects in Canberra, has always been our strength. This ensures our ability to deliver home designs tailored to your specific requirements.</p>
    </div>
    <div class="feature">
      <div class="feature-icon">
        <svg width="52" height="52" viewBox="0 0 52 52"><rect x="10" y="6" width="30" height="40" fill="none" stroke="#c41f2f" stroke-width="4"/><path d="M16 16h18M16 24h18M16 32h10" stroke="#c41f2f" stroke-width="3"/><path d="M30 44l14-14" stroke="#c41f2f" stroke-width="5"/></svg>
      </div>
      <h3>Reliable Contractors</h3>
      <p>Working with the best contractors in the industry enables us to provide you with construction services that are on time and on budget.</p>
    </div>
  </div>
</section>

<section class="touch">
  <div class="touch-photo" role="img" aria-label="Dark photo of a hand holding a smartphone"></div>
  <div class="touch-inner">
    <h2>Get In Touch With Us</h2>
    <p class="intro">Our vision is to build homes to the highest standards.<br>We're a boutique building company in Canberra, that has built many residential properties.</p>
    <p class="gap">Being in the industry for many years has enabled us to master the art of designing and constructing stylish homes that are not only aesthetically pleasing but also affordable.</p>
    <div class="call">
      <span>CALL US NOW!</span>
      <span class="call-icon"><svg width="26" height="26" viewBox="0 0 24 24" fill="#fff"><path d="M6.6 10.8a15 15 0 006.6 6.6l2.2-2.2c.3-.3.7-.4 1-.2 1.1.4 2.3.6 3.6.6.6 0 1 .4 1 1V20c0 .6-.4 1-1 1A17 17 0 013 4c0-.6.4-1 1-1h3.5c.6 0 1 .4 1 1 0 1.3.2 2.5.6 3.6.1.3 0 .7-.2 1z"/></svg></span>
      <span>041 7 38 2 960</span>
    </div>
    <a class="btn">Contact Us</a>
  </div>
</section>

<section class="services">
  <h2 class="section-title">Our <span class="red">Services</span></h2>
  <p class="lead">Lorem Ipsum is simply dummy text of the printing and typesetting industry. Lorem Ipsum has been the industry's standard dummy text ever since the 1500.</p>
  <div class="service-list">
    <div class="service"><svg width="52" height="48" viewBox="0 0 52 48" fill="#c41f2f"><rect x="4" y="14" width="18" height="34"/><rect x="26" y="2" width="22" height="46"/><g fill="#fff"><rect x="9" y="20" width="3" height="4"/><rect x="14" y="20" width="3" height="4"/><rect x="9" y="30" width="3" height="4"/><rect x="14" y="30" width="3" height="4"/><rect x="31" y="10" width="4" height="4"/><rect x="39" y="10" width="4" height="4"/><rect x="31" y="20" width="4" height="4"/><rect x="39" y="20" width="4" height="4"/><rect x="31" y="30" width="4" height="4"/><rect x="39" y="30" width="4" height="4"/></g></svg>General<br>Builder</div>
    <div class="service"><svg width="52" height="48" viewBox="0 0 52 48" fill="#c41f2f"><path d="M26 2L2 24h7v22h12V32h10v14h12V24h7z"/></svg>House<br>Extensions</div>
    <div class="service"><svg width="52" height="48" viewBox="0 0 52 48"><path d="M10 44L38 14M14 4l10 10-6 6L8 10" stroke="#c41f2f" stroke-width="6" fill="none"/><path d="M42 44L16 18M36 4a8 8 0 0 0 8 12" stroke="#c41f2f" stroke-width="6" fill="none"/></svg>Refurbishment</div>
    <div class="service"><svg width="52" height="48" viewBox="0 0 52 48" fill="none" stroke="#c41f2f" stroke-width="4"><rect x="30" y="4" width="14" height="14" rx="2"/><path d="M37 18v8c0 6-8 6-8 12s-10 6-10 0V30"/><rect x="12" y="30" width="14" height="12" rx="2" fill="#c41f2f"/></svg>Electricity</div>
    <div class="service"><svg width="52" height="48" viewBox="0 0 52 48" fill="#c41f2f"><path d="M2 24h48v6c0 8-6 12-14 12H16C8 42 2 38 2 30z"/><rect x="10" y="42" width="4" height="6"/><rect x="38" y="42" width="4" height="6"/><path d="M10 24V8a6 6 0 0 1 12 0" fill="none" stroke="#c41f2f" stroke-width="4"/></svg>Bathrooms</div>
    <div class="service"><svg width="52" height="48" viewBox="0 0 52 48" fill="#c41f2f"><rect x="2" y="20" width="48" height="26"/><rect x="6" y="4" width="40" height="12"/><g fill="#fff"><rect x="8" y="26" width="14" height="16"/><rect x="30" y="26" width="14" height="16"/></g></svg>Kitchens</div>
  </div>
</section>

<section class="portfolio">
  <h2 class="section-title">Cobalt <span class="red">Portfolio</span></h2>
  <div class="tabs">
    <span class="tab active" style="width:104px">All</span>
    <span class="tab" style="width:146px">Building</span>
    <span class="tab" style="width:188px">Bathrooms</span>
    <span class="tab" style="width:188px">Extensions</span>
    <span class="tab" style="width:230px">Refu rbishment</span>
  </div>
  <div class="grid">
    <div class="card"><div class="shot s1" role="img" aria-label="Photo of a modern two-storey home exterior at dusk"></div><div class="cap">Coombs 8/3</div></div>
    <div class="card"><div class="shot s2" role="img" aria-label="Photo of a home with lawn and stepping stones under blue sky"></div><div class="cap">Casey 13/105</div></div>
    <div class="card"><div class="shot s3" role="img" aria-label="Photo of a white minimalist bathroom"></div><div class="cap">Coombs 8/3</div></div>
    <div class="card"><div class="shot s4" role="img" aria-label="Photo of a modern open-plan kitchen"></div><div class="cap">Casey 13/105</div></div>
    <div class="card"><div class="shot s5" role="img" aria-label="Photo of a bright curved white interior with glass walls"></div><div class="cap">Coombs 8/3</div></div>
    <div class="card"><div class="shot s6" role="img" aria-label="Photo of a timber-clad living room with sofa"></div><div class="cap">Casey 13/105</div></div>
    <div class="card"><div class="shot s7" role="img" aria-label="Photo of a contemporary glass office interior"></div><div class="cap">Coombs 8/3</div></div>
    <div class="card"><div class="shot s8" role="img" aria-label="Photo of a sweeping white curved building"></div><div class="cap">Casey 13/105</div></div>
  </div>
</section>

<section class="split">
  <div class="testimonial">
    <h2>Client <span class="red">Testimonial</span></h2>
    <div class="quote-mark">&ldquo;</div>
    <p>Lorem Ipsum is simply dummy text of the printing and typesetting industry. Lorem Ipsum has been the industry's standard dummy text ever since the 1500s, when an unknown printer took a galley of type and scrambled it to make a type specimen book.</p>
    <div class="client">- Client Name</div>
    <div class="arrows">
      <span class="arrow"><svg width="14" height="20" viewBox="0 0 14 20"><path d="M11 2L3 10l8 8" fill="none" stroke="#fff" stroke-width="2"/></svg></span>
      <span class="arrow"><svg width="14" height="20" viewBox="0 0 14 20"><path d="M3 2l8 8-8 8" fill="none" stroke="#fff" stroke-width="2"/></svg></span>
    </div>
  </div>
  <div class="quote-form">
    <h2>Get A <span class="red">Free Quote</span></h2>
    <div class="form">
      <div class="field">Enter Name</div>
      <div class="field">Enter Contact No.</div>
      <div class="field wide">Enter Email</div>
      <div class="field wide msg">Enter Message</div>
      <a class="btn">Submit</a>
    </div>
  </div>
</section>

<section class="banner">
  <p>Get a <b>FREE</b> building estimation today for your next project!</p>
  <a class="cta">Contact Us</a>
</section>

<footer class="footer">
  <div class="footer-top">
    <nav class="footer-nav">
      <span class="active">General Builder</span><span>House Extensions</span><span>Refurbishment</span><span>Electricity</span><span>Bathrooms</span><span>Kitchens</span>
    </nav>
    <div class="social"><span><i></i></span><span><i></i></span></div>
  </div>
  <h4>Contact Us</h4>
  <div class="footer-info">
    <div class="info addr">
      <svg width="16" height="24" viewBox="0 0 16 24" fill="#fff"><path d="M8 0a8 8 0 0 0-8 8c0 6 8 16 8 16s8-10 8-16a8 8 0 0 0-8-8zm0 11a3 3 0 1 1 0-6 3 3 0 0 1 0 6z"/></svg>
      <span>22, Ferris Cres,<br>Narrabundah Canberra, ACT,<br><u>VIEW MAP</u></span>
    </div>
    <div class="info tel">
      <svg width="20" height="20" viewBox="0 0 24 24" fill="#fff"><path d="M6.6 10.8a15 15 0 006.6 6.6l2.2-2.2c.3-.3.7-.4 1-.2 1.1.4 2.3.6 3.6.6.6 0 1 .4 1 1V20c0 .6-.4 1-1 1A17 17 0 013 4c0-.6.4-1 1-1h3.5c.6 0 1 .4 1 1 0 1.3.2 2.5.6 3.6.1.3 0 .7-.2 1z"/></svg>
      <span>0417 382 960</span>
    </div>
    <div class="info mail">
      <svg width="22" height="16" viewBox="0 0 22 16" fill="none" stroke="#fff" stroke-width="2"><rect x="1" y="1" width="20" height="14"/><path d="M1 1l10 8 10-8"/></svg>
      <span>info@cobalthomes.com.au</span>
    </div>
    <div class="copy">
      <span>&copy;</span><span><span class="red">Cobalt Home Builders Canberra</span> - 2016. All Rights Reserved.</span>
    </div>
  </div>
</footer>

</body>
</html>
```